Action Plan - Presentation Template

I want a template that is very design oriented, we are a design company PlinthWorks. My first use is going to be an action plan, but i want this to have a clean hi tech feel. I have attached some of the branding elements. The plan will identify Action Steps and then map them on to a timeline.
Overview: Summary of Project
Goals: what want to accomplish
Solution: how we accomplish those goals
Following that information will be our designs/solutions(I just uploaded a few Torlan & Veskit)
Followed by some
Services: Support solutions
Team: who we are

I uploaded a couple of Old Ones Halvora and Quendral

Target Market(s)

Biotech

Requirements
Must have
• Clean Simple Tech Feel

```html
<!DOCTYPE html>
<html lang="en">
<head>
<meta charset="utf-8">
<title>PlinthWorks Presentation Template</title>
<link href="https://fonts.googleapis.com/css2?family=Montserrat:wght@400;500;600;700;800&display=swap" rel="stylesheet">
<style>
:root{--blue:#16a4ec;--ink:#111;--grey:#e6e7e8;--text:#5a5a5a;--bg:#2b2b2d;--photo-a:#d9d9d9;--photo-b:#9a9a9a}
html,body{margin:0;padding:0;width:891px;height:1200px;overflow:hidden;background:var(--bg)}
body{position:relative;font-family:'Montserrat',sans-serif}
.slide{position:absolute;width:271px;height:153px;background:#fff;overflow:hidden;color:var(--ink)}
.slide>*{position:absolute;margin:0}
.deco{left:0;top:0;width:271px;height:153px}
.photo{background:linear-gradient(135deg,var(--photo-a),var(--photo-b))}
.h{font-weight:500;line-height:1.05;letter-spacing:.01em}
.b{font-weight:800}
.blue{color:var(--blue)}
.p{font-size:3px;line-height:1.4;color:var(--text)}
.p p{margin:0 0 2px}
.foot{right:4px;bottom:3px;display:flex;align-items:center;gap:2px;font-size:3.6px;font-weight:700;letter-spacing:.02em}
.foot i{font-style:normal;background:var(--blue);color:#fff;padding:.6px 2px}
.brand{font-weight:700;letter-spacing:.02em}
.li{font-size:5.6px;color:#444;line-height:2.05}
.lbl{font-size:4.4px;font-weight:700}
.tiny{font-size:2.6px;line-height:1.35;color:var(--text)}
</style>
</head>
<body>

<!-- 01 cover -->
<section class="slide" style="left:29px;top:31px">
  <div class="photo" style="left:95px;top:0;width:176px;height:153px;background:linear-gradient(90deg,#fff 0%,#e4e4e4 25%,#a8a8a8 100%)" role="img" aria-label="Photo of two business colleagues smiling at a desk"></div>
  <svg class="deco" viewBox="0 0 271 153"><circle cx="200" cy="126" r="9" fill="var(--blue)"/><circle cx="270" cy="165" r="48" fill="none" stroke="var(--ink)" stroke-width="2"/><circle cx="225" cy="-6" r="24" fill="var(--blue)"/></svg>
  <div class="brand" style="left:12px;top:13px;font-size:13px">PLINTHWORKS</div>
  <div class="h" style="left:12px;top:70px;font-size:7px">PRESENTATION</div>
  <div class="h b" style="left:12px;top:79px;font-size:17px">BUSINESS</div>
  <div class="h b blue" style="left:12px;top:97px;font-size:17px;font-weight:700">MARKETING</div>
  <div style="left:12px;top:124px;font-size:4.6px;letter-spacing:.2em;font-weight:600">www.plinthworks.co</div>
  <div style="left:12px;top:121px;width:80px;height:.5px;background:var(--ink)"></div>
  <div style="left:12px;top:132px;width:7px;height:7px;background:var(--blue)"></div>
</section>

<!-- 02 contents -->
<section class="slide" style="left:312px;top:31px">
  <div class="photo" style="left:0;top:0;width:90px;height:153px" role="img" aria-label="Photo of two colleagues reviewing a folder"></div>
  <svg class="deco" viewBox="0 0 271 153"><circle cx="111" cy="26" r="11" fill="none" stroke="var(--ink)" stroke-width="1"/><circle cx="128" cy="15" r="4" fill="var(--blue)"/><circle cx="262" cy="12" r="22" fill="var(--blue)"/><circle cx="262" cy="12" r="26" fill="none" stroke="var(--ink)" stroke-width="1.4"/></svg>
  <div class="h b blue" style="left:82px;top:68px;font-size:12.5px;background:#fff;padding:1px 3px">Contents</div>
  <div style="left:152px;top:26px;width:100px">
    <div class="lbl" style="font-size:5.6px"><span class="blue">1.</span> Lorem ipsum</div>
    <div class="tiny" style="padding-left:9px;margin-bottom:11px">Steps set out clearly, one owner per task and goal.</div>
    <div class="lbl" style="font-size:5.6px"><span class="blue">2.</span> <span class="blue">Lorem ipsum</span></div>
    <div class="tiny" style="padding-left:9px;margin-bottom:11px">Steps set out clearly, one owner per task and goal.</div>
    <div class="lbl" style="font-size:5.6px"><span class="blue">3.</span> Lorem ipsum</div>
    <div class="tiny" style="padding-left:9px;margin-bottom:11px">Steps set out clearly, one owner per task and goal.</div>
    <div class="lbl" style="font-size:5.6px"><span class="blue">4.</span> <span class="blue">Lorem ipsum</span></div>
    <div class="tiny" style="padding-left:9px">Steps set out clearly, one owner per task and goal.</div>
  </div>
  <div class="foot"><span>PLINTHWORKS</span><i>02</i></div>
</section>

<!-- 03 part one -->
<section class="slide" style="left:596px;top:31px">
  <div class="photo" style="left:0;top:0;width:271px;height:153px;background:linear-gradient(120deg,#f0f0f0,#c9c9c9)" role="img" aria-label="Faded photo of hands holding a phone"></div>
  <svg class="deco" viewBox="0 0 271 153"><circle cx="-2" cy="106" r="16" fill="var(--ink)"/><circle cx="31" cy="150" r="12" fill="var(--blue)"/><circle cx="268" cy="8" r="30" fill="none" stroke="var(--blue)" stroke-width="1.6"/><circle cx="250" cy="28" r="6" fill="var(--ink)"/><circle cx="136" cy="68" r="58" fill="none" stroke="var(--ink)" stroke-width="1.4"/><circle cx="136" cy="68" r="53" fill="var(--blue)"/><circle cx="104" cy="33" r="16" fill="var(--ink)"/><text x="104" y="37" fill="#fff" font-size="11" font-weight="700" text-anchor="middle" font-family="Montserrat,sans-serif">01</text></svg>
  <div class="h b" style="left:93px;top:50px;font-size:17px;color:#fff;font-weight:700">Part One.</div>
  <div class="p" style="left:93px;top:72px;width:84px;color:#fff;font-size:3.4px">A short summary of the project scope, the goals it serves and the result the team expects.</div>
  <div class="foot"><span>PLINTHWORKS</span><i>03</i></div>
</section>

<!-- 04 domain -->
<section class="slide" style="left:29px;top:196px">
  <svg class="deco" viewBox="0 0 271 153"><circle cx="254" cy="11" r="5" fill="var(--blue)"/><circle cx="284" cy="30" r="20" fill="none" stroke="var(--ink)" stroke-width="1.4"/><circle cx="133" cy="160" r="22" fill="none" stroke="var(--ink)" stroke-width="1.4"/><circle cx="133" cy="162" r="19" fill="var(--blue)"/></svg>
  <div class="h" style="left:14px;top:22px;font-size:9px">LOREM IPSUM</div>
  <div class="h b blue" style="left:14px;top:33px;font-size:9px">DOLOR SIT AMET</div>
  <div class="p" style="left:14px;top:48px;width:130px">
    <p>• <b class="blue">Lorem ipsum</b> : each task has an owner, a start date and a clear end result.</p>
    <p>• <b class="blue">Lorem ipsum</b> : each task has an owner, a start date and a clear end result to meet in the plan.</p>
    <p>• <b class="blue">Lorem ipsum</b> : each task has an owner, a start date and a clear end result to meet.</p>
    <p>• <b class="blue">Lorem ipsum</b> : each task has an owner and a clear end result.</p>
    <p>• <b class="blue">Lorem ipsum</b> : each task has an owner, a start date and a clear end result to meet.</p>
  </div>
  <div class="h blue" style="left:154px;top:21px;font-size:7.6px">WHAT'S A DOMAIN?</div>
  <div class="h blue" style="left:154px;top:32px;font-size:7.6px">IT'S THAT NAME UP</div>
  <div class="h b" style="left:154px;top:43px;font-size:7.6px">IN THE ADDRESS BAR.</div>
  <div class="li" style="left:154px;top:56px"><span class="blue">▪</span> Fits your business or products<br><span class="blue">▪</span> Is easy to spell and remember<br><span class="blue">▪</span> Fits your business or products<br><span class="blue">▪</span> Is easy to spell and remember<br><span class="blue">▪</span> Fits your business or products<br><span class="blue">▪</span> Is easy to spell and remember</div>
  <div class="foot"><span>PLINTHWORKS</span><i>04</i></div>
</section>

<!-- 05 education -->
<section class="slide" style="left:312px;top:196px">
  <div style="left:40px;top:35px;width:190px;height:80px;background:radial-gradient(ellipse,#f1f1f1 40%,#fff 72%)" role="img" aria-label="Faint world map background"></div>
  <svg class="deco" viewBox="0 0 271 153"><circle cx="248" cy="16" r="8" fill="var(--blue)"/><circle cx="2" cy="100" r="16" fill="var(--blue)"/><circle cx="268" cy="116" r="16" fill="var(--blue)"/><circle cx="268" cy="116" r="20" fill="none" stroke="var(--ink)" stroke-width="1.2"/>
    <rect x="54" y="38" width="46" height="68" rx="6" fill="#fff" stroke="var(--ink)" stroke-width="1.4"/>
    <rect x="118" y="38" width="46" height="72" rx="6" fill="#fff" stroke="var(--blue)" stroke-width="1.4"/>
    <rect x="182" y="38" width="46" height="68" rx="6" fill="#fff" stroke="var(--blue)" stroke-width="1.4"/>
    <path d="M100 56 L104 48 L104 40" fill="none" stroke="var(--ink)" stroke-width="1.2"/><circle cx="104" cy="56" r="2" fill="var(--ink)"/>
    <path d="M164 56 L182 100" stroke="var(--blue)" stroke-width="1.2"/><circle cx="115" cy="106" r="2" fill="var(--blue)"/><circle cx="179" cy="106" r="2" fill="var(--blue)"/>
    <path d="M68 66 q4-6 8 0 q-1 3-2 4 h-4 q-1-1-2-4z" fill="none" stroke="var(--blue)" stroke-width=".8"/>
    <rect x="136" y="51" width="9" height="6" fill="none" stroke="var(--blue)" stroke-width=".8"/><path d="M136 51 l4.5 3.5 l4.5-3.5" fill="none" stroke="var(--blue)" stroke-width=".8"/>
    <path d="M200 58 l3-4 l3 2 l4-5 M199 51 v8 h12" fill="none" stroke="var(--blue)" stroke-width=".8"/></svg>
  <div class="h" style="left:11px;top:8px;font-size:9.8px;font-weight:600">OUR COMPANY <span class="blue b">EDUCATION</span></div>
  <div class="lbl blue" style="left:54px;top:64px;width:46px;text-align:center">IDEA</div>
  <div class="lbl blue" style="left:118px;top:64px;width:46px;text-align:center">PROMOTION</div>
  <div class="lbl blue" style="left:182px;top:64px;width:46px;text-align:center">GROWTH</div>
  <div class="tiny" style="left:57px;top:72px;width:40px;text-align:center">Gather needs, set goals and sketch the first ideas for the team.</div>
  <div class="tiny" style="left:121px;top:72px;width:40px;text-align:center">Share the plan, test it with users and tune the message.</div>
  <div class="tiny" style="left:185px;top:72px;width:40px;text-align:center">Measure results, scale what works and plan the next step.</div>
  <div class="p" style="left:38px;top:120px;width:196px;text-align:center">Every step in this plan links a task to a goal and a date, so the team can track progress and see how each stage builds on the one before it.</div>
  <div class="foot"><span>PLINTHWORKS</span><i>05</i></div>
</section>

<!-- 06 data -->
<section class="slide" style="left:596px;top:196px">
  <div style="left:15px;top:14px;width:127px;height:124px;background:var(--grey)"></div>
  <svg class="deco" viewBox="0 0 271 153"><circle cx="255" cy="53" r="5" fill="var(--blue)"/><circle cx="147" cy="32" r="11" fill="var(--blue)" stroke="#fff" stroke-width="1.6"/><circle cx="147" cy="75" r="11" fill="var(--blue)" stroke="#fff" stroke-width="1.6"/><circle cx="147" cy="118" r="11" fill="var(--blue)" stroke="#fff" stroke-width="1.6"/>
    <rect x="142" y="28" width="9" height="6" fill="none" stroke="#fff" stroke-width=".8"/><path d="M147 34 v3 M144 37 h6" stroke="#fff" stroke-width=".8"/>
    <path d="M142 77 a3 3 0 0 1 2-5 a4 4 0 0 1 7 1 a2.5 2.5 0 0 1 0 4z" fill="#fff"/>
    <circle cx="143" cy="121" r="1.5" fill="#fff"/><circle cx="147" cy="116" r="1.5" fill="#fff"/><circle cx="151" cy="119" r="1.5" fill="#fff"/><path d="M143 121 L147 116 L151 119" stroke="#fff" stroke-width=".7" fill="none"/></svg>
  <div class="h" style="left:25px;top:25px;font-size:11px">DATA OUR</div>
  <div class="h b blue" style="left:25px;top:38px;font-size:11px">COMPANY</div>
  <div class="p" style="left:24px;top:57px;width:108px"><p>Data shows where the project stands today, what the team has learned so far and which goals need the most attention in the next phase of the plan. Each figure links back to a task, an owner and a date so nothing is lost along the way.</p><p>Reports are shared each week with the whole team and the client, so every choice can be traced to a clear goal.</p></div>
  <div style="left:163px;top:19px;width:100px"><div class="lbl" style="font-size:5.4px">Lorem ipsum</div><div class="tiny">Short note on the data set, the source and the key trend it shows for the team.</div></div>
  <div style="left:163px;top:62px;width:100px"><div class="lbl" style="font-size:5.4px">Lorem ipsum</div><div class="tiny">Short note on the data set, the source and the key trend it shows for the team.</div></div>
  <div style="left:163px;top:104px;width:100px"><div class="lbl" style="font-size:5.4px">Lorem ipsum</div><div class="tiny">Short note on the data set, the source and the key trend it shows for the team.</div></div>
  <div class="foot"><span>PLINTHWORKS</span><i>06</i></div>
</section>

<!-- 07 portfolio -->
<section class="slide" style="left:29px;top:362px">
  <div class="photo" style="left:0;top:0;width:22px;height:153px" role="img" aria-label="Photo of office buildings"></div>
  <div style="left:22px;top:0;width:106px;height:153px;background:var(--ink)"></div>
  <div class="photo" style="left:128px;top:0;width:143px;height:153px;background:linear-gradient(135deg,#ececec,#8d8d8d)" role="img" aria-label="Photo of a businessman in a suit with arms crossed"></div>
  <svg class="deco" viewBox="0 0 271 153"><circle cx="258" cy="12" r="18" fill="var(--blue)"/><circle cx="254" cy="18" r="22" fill="none" stroke="var(--ink)" stroke-width="1.3"/><circle cx="260" cy="153" r="12" fill="none" stroke="var(--ink)" stroke-width="1.2"/><path d="M28 94 l4 2.5 l-4 2.5z" fill="var(--blue)"/><path d="M28 110 l4 2.5 l-4 2.5z" fill="none" stroke="var(--blue)" stroke-width=".6"/></svg>
  <div class="h" style="left:27px;top:17px;font-size:6.6px;color:#fff">PORTFOLIO OF</div>
  <div class="h b blue" style="left:27px;top:25px;font-size:13.5px">PROJECTS</div>
  <div class="p" style="left:27px;top:42px;width:96px;color:#ddd;text-align:justify"><p>A selection of past work shows how the studio turns goals into clear designs. Each project lists the brief, the steps taken and the final result delivered to the client.</p><p>Teams worked in short stages, tested ideas early and kept the plan in view so every choice served the goal and the date.</p></div>
  <div class="tiny" style="left:36px;top:93px;width:86px;color:#ddd">Project note for the first case study in this set.</div>
  <div class="tiny" style="left:36px;top:109px;width:86px;color:#ddd">Project note for the second case study in this set.</div>
  <div class="foot" style="color:var(--ink)"><span>PLINTHWORKS</span><i>07</i></div>
</section>

<!-- 08 market -->
<section class="slide" style="left:312px;top:362px">
  <svg class="deco" viewBox="0 0 271 153"><circle cx="16" cy="154" r="5" fill="var(--blue)"/><circle cx="268" cy="84" r="14" fill="var(--blue)"/><circle cx="264" cy="86" r="18" fill="none" stroke="var(--ink)" stroke-width="1.2"/>
    <g font-family="Montserrat,sans-serif" font-size="3" fill="#333">
      <text x="141" y="15" font-size="3.4" font-weight="600">CONSECTETUER ADIPISCING</text>
      <text x="133" y="22">60</text><text x="133" y="30">50</text><text x="133" y="38">40</text><text x="133" y="46">30</text><text x="133" y="54">20</text><text x="133" y="62">10</text><text x="135" y="70">0</text>
      <text x="150" y="75">JAN</text><text x="172" y="75">FEB</text><text x="194" y="75">MAR</text><text x="216" y="75">APR</text></g>
    <g stroke="#ccc" stroke-width=".3"><path d="M139 21h110M139 29h110M139 37h110M139 45h110M139 53h110M139 61h110M139 21v48M249 21v48"/></g>
    <path d="M139 69h110" stroke="#333" stroke-width=".5"/>
    <rect x="148" y="37" width="11" height="32" fill="var(--ink)"/><rect x="170" y="23" width="11" height="46" fill="var(--blue)"/><rect x="192" y="57" width="11" height="12" fill="var(--ink)"/><rect x="214" y="32" width="11" height="37" fill="var(--blue)"/>
    <ellipse cx="57" cy="119" rx="31" ry="14" fill="#0b7fc0"/><ellipse cx="57" cy="114" rx="31" ry="14" fill="var(--blue)"/><path d="M57 100 A31 14 0 0 1 88 114 L71 114 A14 6 0 0 0 57 108z" fill="var(--ink)"/><path d="M62 127.7 A31 14 0 0 0 88 114 L71 114 A14 6 0 0 1 60 119.8z" fill="var(--ink)"/><ellipse cx="57" cy="114" rx="14" ry="6" fill="#fff"/>
    <g font-family="Montserrat,sans-serif" font-size="4.5" font-weight="700" fill="#fff"><text x="27" y="116">40%</text><text x="65" y="106">20%</text><text x="76" y="118">20%</text><text x="62" y="126">20%</text></g>
    <circle cx="102" cy="95" r="1.8" fill="var(--blue)"/><circle cx="180" cy="95" r="1.8" fill="var(--ink)"/><circle cx="102" cy="118" r="1.8" fill="var(--ink)"/><circle cx="180" cy="118" r="1.8" fill="var(--blue)"/></svg>
  <div class="h b" style="left:13px;top:10px;font-size:12px">MARKET</div>
  <div class="h b blue" style="left:13px;top:23px;font-size:12px">OPPORTUNITIES</div>
  <div class="p" style="left:13px;top:41px;width:108px"><p>Biotech teams need clear plans they can share. This section shows where demand is growing and which segments the studio can serve first with the least risk.</p><p>Key figures are tracked by month against the plan.</p></div>
  <div style="left:107px;top:92px;width:64px"><div class="lbl blue">Lorem ipsum</div><div class="tiny">Market share held by the lead segment this quarter.</div></div>
  <div style="left:185px;top:92px;width:64px"><div class="lbl">Lorem ipsum</div><div class="tiny">Market share held by the second segment this quarter.</div></div>
  <div style="left:107px;top:115px;width:64px"><div class="lbl">Lorem ipsum</div><div class="tiny">Market share held by the third segment this quarter.</div></div>
  <div style="left:185px;top:115px;width:64px"><div class="lbl blue">Lorem ipsum</div><div class="tiny">Market share held by new entrants this quarter.</div></div>
  <div class="foot"><span>PLINTHWORKS</span><i>08</i></div>
</section>

<!-- 09 overview -->
<section class="slide" style="left:596px;top:362px">
  <svg class="deco" viewBox="0 0 271 153"><circle cx="113" cy="-8" r="18" fill="none" stroke="var(--ink)" stroke-width="1.2"/><circle cx="113" cy="-10" r="15" fill="var(--blue)"/><circle cx="258" cy="90" r="4" fill="var(--blue)"/><circle cx="270" cy="150" r="14" fill="none" stroke="var(--ink)" stroke-width="1.2"/>
    <g font-family="Montserrat,sans-serif" font-size="3" fill="#333"><text x="139" y="25">60</text><text x="139" y="33">50</text><text x="139" y="41">40</text><text x="139" y="49">30</text><text x="139" y="57">20</text><text x="139" y="65">10</text><text x="141" y="75">0</text>
      <text x="158" y="80">JAN</text><text x="181" y="80">FEB</text><text x="204" y="80">MAR</text><text x="227" y="80">APR</text>
      <text x="13" y="90">60</text><text x="13" y="96">50</text><text x="13" y="102">40</text><text x="13" y="108">30</text><text x="13" y="114">20</text><text x="13" y="120">10</text><text x="15" y="127">0</text></g>
    <rect x="147" y="22" width="107" height="52" fill="none" stroke="#ccc" stroke-width=".3"/>
    <rect x="152" y="41" width="3" height="33" fill="var(--ink)"/><rect x="157" y="33" width="3" height="41" fill="var(--blue)"/>
    <rect x="174" y="65" width="3" height="9" fill="var(--ink)"/><rect x="179" y="45" width="3" height="29" fill="var(--blue)"/>
    <rect x="197" y="26" width="3" height="48" fill="var(--ink)"/><rect x="202" y="63" width="3" height="11" fill="var(--blue)"/>
    <rect x="220" y="32" width="3" height="42" fill="var(--blue)"/><rect x="225" y="52" width="3" height="22" fill="var(--ink)"/>
    <path d="M20 88v38h100" fill="none" stroke="#ccc" stroke-width=".4"/>
    <polyline points="22,120 34,126 46,110 58,96 70,105 82,112 94,103 106,99 118,115" fill="none" stroke="var(--blue)" stroke-width=".8"/>
    <polyline points="22,124 34,120 46,114 58,118 70,100 82,108 94,114 106,104 118,102" fill="none" stroke="var(--ink)" stroke-width=".8"/>
    <g fill="var(--ink)"><circle cx="46" cy="114" r="1"/><circle cx="58" cy="118" r="1"/><circle cx="70" cy="100" r="1"/><circle cx="106" cy="104" r="1"/></g>
    <g fill="var(--blue)"><circle cx="58" cy="96" r="1"/><circle cx="82" cy="112" r="1"/><circle cx="106" cy="99" r="1"/></g>
    <circle cx="136" cy="97" r="1.6" fill="var(--ink)"/><circle cx="202" cy="97" r="1.6" fill="var(--blue)"/><circle cx="136" cy="116" r="1.6" fill="var(--blue)"/><circle cx="202" cy="116" r="1.6" fill="var(--ink)"/></svg>
  <div class="h b" style="left:13px;top:14px;font-size:10px">COMPANY</div>
  <div class="h b blue" style="left:13px;top:24px;font-size:13px">OVERVIEW</div>
  <div class="p" style="left:13px;top:42px;width:110px"><p>An overview of the studio: how work is planned, how goals are set and how results are shared with the client in each phase.</p><p>Monthly figures compare plan and actual.</p></div>
  <div style="left:140px;top:95px;width:55px"><div class="lbl" style="font-size:3.8px">Lorem ipsum</div><div class="tiny">Planned hours for the phase.</div></div>
  <div style="left:206px;top:95px;width:55px"><div class="lbl blue" style="font-size:3.8px">Lorem ipsum</div><div class="tiny">Actual hours for the phase.</div></div>
  <div style="left:140px;top:114px;width:55px"><div class="lbl blue" style="font-size:3.8px">Lorem ipsum</div><div class="tiny">Tasks done on time.</div></div>
  <div style="left:206px;top:114px;width:55px"><div class="lbl" style="font-size:3.8px">Lorem ipsum</div><div class="tiny">Tasks moved to later.</div></div>
  <div class="foot"><span>PLINTHWORKS</span><i>09</i></div>
</section>

<!-- 10 pins -->
<section class="slide" style="left:29px;top:528px">
  <svg class="deco" viewBox="0 0 271 153"><circle cx="247" cy="17" r="8" fill="var(--blue)"/><circle cx="290" cy="45" r="22" fill="none" stroke="var(--ink)" stroke-width="1.4"/><circle cx="-3" cy="101" r="13" fill="var(--blue)"/><circle cx="-3" cy="101" r="16" fill="none" stroke="var(--ink)" stroke-width="1.2"/>
    <polyline points="51,37 91,50 131,31 171,29 211,37" fill="none" stroke="#999" stroke-width=".4" stroke-dasharray="1 1"/>
    <path d="M51 37 L35 79 L51 90 L67 79z" fill="var(--ink)"/><path d="M91 50 L75 79 L91 90 L107 79z" fill="var(--blue)"/><path d="M131 31 L115 79 L131 90 L147 79z" fill="var(--ink)"/><path d="M171 29 L155 79 L171 90 L187 79z" fill="var(--blue)"/><path d="M211 37 L195 79 L211 90 L227 79z" fill="var(--ink)"/>
    <g fill="#fff"><circle cx="40" cy="82" r="3"/><circle cx="80" cy="82" r="3"/><circle cx="120" cy="82" r="3"/><circle cx="160" cy="82" r="3"/><circle cx="200" cy="82" r="3"/></g>
    <g fill="#fff" stroke="var(--ink)" stroke-width=".8"><circle cx="51" cy="37" r="1.6"/><circle cx="91" cy="50" r="1.6"/><circle cx="131" cy="31" r="1.6"/><circle cx="171" cy="29" r="1.6"/><circle cx="211" cy="37" r="1.6"/></g>
    <g font-family="Montserrat,sans-serif" font-size="3.4" font-weight="700" text-anchor="middle"><text x="51" y="33">$1000</text><text x="91" y="46">$750</text><text x="131" y="27">$1200</text><text x="171" y="25">$1400</text><text x="211" y="33">$1100</text>
      <g fill="#fff" font-size="3.8"><text transform="translate(54 70) rotate(-90)">Title One</text><text transform="translate(94 70) rotate(-90)">Title Two</text><text transform="translate(134 70) rotate(-90)">Title Three</text><text transform="translate(174 70) rotate(-90)">Title Four</text><text transform="translate(214 70) rotate(-90)">Title Five</text></g>
      <g font-size="2.8" fill="#333"><text x="51" y="100">2014</text><text x="91" y="100">2016</text><text x="131" y="100">2018</text><text x="171" y="100">2020</text><text x="211" y="100">2022</text></g></g>
    <path d="M40 94 H222" stroke="#999" stroke-width=".4"/>
    <g fill="none" stroke-width="1"><path d="M46 104l5 4l5-4" stroke="var(--ink)"/><path d="M86 104l5 4l5-4" stroke="var(--blue)"/><path d="M126 104l5 4l5-4" stroke="var(--ink)"/><path d="M166 104l5 4l5-4" stroke="var(--blue)"/><path d="M206 104l5 4l5-4" stroke="var(--ink)"/></g></svg>
  <div class="h" style="left:15px;top:11px;font-size:8.4px;font-weight:700">LOREM IPSUM <span class="blue">DOLOR SIT AMET</span></div>
  <div class="tiny" style="left:31px;top:114px;width:36px">Milestone note with the budget spent by this date.</div>
  <div class="tiny" style="left:71px;top:114px;width:36px">Milestone note with the budget spent by this date.</div>
  <div class="tiny" style="left:111px;top:114px;width:36px">Milestone note with the budget spent by this date.</div>
  <div class="tiny" style="left:151px;top:114px;width:36px">Milestone note with the budget spent by this date.</div>
  <div class="tiny" style="left:191px;top:114px;width:36px">Milestone note with the budget spent by this date.</div>
  <div class="foot"><span>PLINTHWORKS</span><i>10</i></div>
</section>

<!-- 11 steps -->
<section class="slide" style="left:312px;top:528px">
  <svg class="deco" viewBox="0 0 271 153"><circle cx="262" cy="4" r="12" fill="var(--blue)"/><circle cx="262" cy="4" r="15" fill="none" stroke="var(--ink)" stroke-width="1.2"/><circle cx="29" cy="158" r="7" fill="var(--blue)"/>
    <polygon points="124,37 146,14 168,37 158,37 158,118 136,128 136,45 124,45" fill="var(--blue)"/><polygon points="158,37 168,37 168,110 158,118" fill="#0b7fc0"/>
    <rect x="57" y="52" width="78" height="14" fill="var(--blue)"/><rect x="45" y="69" width="78" height="14" fill="var(--ink)"/><rect x="33" y="87" width="78" height="14" fill="var(--blue)"/><rect x="20" y="106" width="78" height="14" fill="var(--ink)"/>
    <polygon points="97,106 118,96 140,106 119,116" fill="#333"/><polygon points="97,106 119,116 119,140 97,130" fill="var(--ink)"/><polygon points="119,116 140,106 140,130 119,140" fill="#222"/>
    <polygon points="112,90 126,84 140,90 126,96" fill="#0b7fc0"/><polygon points="112,90 126,96 126,125 112,118" fill="var(--blue)"/>
    <polygon points="122,70 136,64 150,70 136,76" fill="#333"/><polygon points="122,70 136,76 136,115 122,108" fill="var(--ink)"/>
    <g font-family="Montserrat,sans-serif" font-weight="800" font-size="7" fill="#fff" font-style="italic"><text x="60" y="62">50%</text><text x="48" y="79">40%</text><text x="36" y="97">30%</text><text x="23" y="116">20%</text></g>
    <g font-family="Montserrat,sans-serif" font-weight="700" font-size="3.6" fill="#fff"><text transform="translate(112 138) rotate(-75)">Step 01</text><text transform="translate(125 126) rotate(-75)">Step 02</text><text transform="translate(137 112) rotate(-75)">Step 03</text><text transform="translate(150 98) rotate(-75)">Step 04</text></g>
    <g fill="var(--ink)"><circle cx="184" cy="41" r="1.8"/><circle cx="184" cy="63" r="1.8"/><circle cx="184" cy="86" r="1.8"/><circle cx="184" cy="108" r="1.8"/></g></svg>
  <div class="tiny" style="left:82px;top:54px;width:50px;color:#fff">Goal met by the end of phase four.</div>
  <div class="tiny" style="left:70px;top:71px;width:50px;color:#fff">Goal met by the end of phase three.</div>
  <div class="tiny" style="left:55px;top:89px;width:50px;color:#fff">Goal met by the end of phase two.</div>
  <div class="tiny" style="left:43px;top:108px;width:50px;color:#fff">Goal met by the end of phase one.</div>
  <div class="h" style="left:23px;top:15px;font-size:10.5px">STARTING</div>
  <div class="h b blue" style="left:23px;top:28px;font-size:10.5px">NEW SECTION</div>
  <div style="left:191px;top:38px;width:70px"><div class="lbl blue">Lorem ipsum</div><div class="tiny">Action step with owner and due date for this stage.</div></div>
  <div style="left:191px;top:60px;width:70px"><div class="lbl">Lorem ipsum</div><div class="tiny">Action step with owner and due date for this stage.</div></div>
  <div style="left:191px;top:83px;width:70px"><div class="lbl blue">Lorem ipsum</div><div class="tiny">Action step with owner and due date for this stage.</div></div>
  <div style="left:191px;top:105px;width:70px"><div class="lbl">Lorem ipsum</div><div class="tiny">Action step with owner and due date for this stage.</div></div>
  <div class="foot"><span>PLINTHWORKS</span><i>11</i></div>
</section>

<!-- 12 intelligence -->
<section class="slide" style="left:596px;top:528px">
  <div style="left:18px;top:13px;width:92px;height:1.4px;background:var(--ink)"></div>
  <div class="photo" style="left:0;top:18px;width:157px;height:112px;background:linear-gradient(135deg,#9d9d9d,#d6d6d6 60%,#8a8a8a)" role="img" aria-label="Photo of a team joining fists over a tech glow"></div>
  <div style="left:0;top:130px;width:157px;height:1.6px;background:var(--blue)"></div>
  <svg class="deco" viewBox="0 0 271 153"><circle cx="255" cy="9" r="4.5" fill="var(--blue)"/><path d="M169 104 l4 2.5 l-4 2.5z" fill="var(--ink)"/><path d="M169 121 l4 2.5 l-4 2.5z" fill="none" stroke="var(--ink)" stroke-width=".6"/></svg>
  <div class="h" style="left:168px;top:20px;font-size:8.5px">ACTIVE</div>
  <div class="h b blue" style="left:168px;top:30px;font-size:8.5px">INTELLIGENCE</div>
  <div class="p" style="left:168px;top:42px;width:92px;text-align:justify"><p>Shared data helps the team act fast. Each insight is tied to a goal, so the plan can change when new results come in from the field and the lab.</p><p>Weekly reviews keep the steps on track and show where support is needed most, so no task waits too long.</p></div>
  <div class="tiny" style="left:176px;top:102px;width:84px">Note on how insights feed the next action step.</div>
  <div class="tiny" style="left:176px;top:119px;width:84px">Note on how insights feed the next action step.</div>
  <div class="foot"><span>PLINTHWORKS</span><i>12</i></div>
</section>

<!-- 13 roadmap -->
<section class="slide" style="left:29px;top:693px">
  <svg class="deco" viewBox="0 0 271 153"><circle cx="6" cy="5" r="13" fill="var(--blue)"/><circle cx="6" cy="5" r="16" fill="none" stroke="var(--ink)" stroke-width="1.2"/><circle cx="256" cy="9" r="4" fill="var(--blue)"/><circle cx="296" cy="34" r="24" fill="none" stroke="var(--ink)" stroke-width="1.3"/><circle cx="170" cy="160" r="14" fill="var(--blue)"/><circle cx="170" cy="160" r="17" fill="none" stroke="var(--ink)" stroke-width="1.2"/>
    <path d="M232 118 C200 116 160 112 137 103 C124 96 128 80 134 70 C146 58 170 62 178 48" fill="none" stroke="var(--blue)" stroke-width="1.2"/>
    <path d="M122 28 C118 40 104 38 100 45 C96 52 118 58 126 52" fill="none" stroke="var(--blue)" stroke-width="1"/>
    <path d="M232 86 V118 M178 40 V48 M134 64 V70" stroke="var(--ink)" stroke-width=".8" stroke-dasharray="1 1"/><circle cx="232" cy="118" r="1.8" fill="var(--ink)"/>
    <circle cx="231" cy="70" r="19" fill="var(--ink)"/><circle cx="231" cy="70" r="15" fill="#fff"/><circle cx="134" cy="54" r="12" fill="var(--ink)"/><circle cx="134" cy="54" r="9" fill="#fff"/><circle cx="178" cy="33" r="9" fill="var(--ink)"/><circle cx="178" cy="33" r="6.5" fill="#fff"/><circle cx="100" cy="36" r="6" fill="var(--ink)"/><circle cx="100" cy="36" r="4.3" fill="#fff"/><circle cx="121" cy="24" r="4.2" fill="var(--ink)"/><circle cx="121" cy="24" r="3" fill="#fff"/><circle cx="81" cy="19" r="3.4" fill="var(--ink)"/><circle cx="81" cy="19" r="2.4" fill="#fff"/>
    <g font-family="Montserrat,sans-serif" font-weight="700" fill="var(--blue)" text-anchor="middle"><text x="231" y="79" font-size="25">1</text><text x="134" y="59" font-size="13">2</text><text x="178" y="37" font-size="9">3</text><text x="100" y="38.5" font-size="6">4</text><text x="121" y="25.6" font-size="4.2">5</text><text x="81" y="20.2" font-size="3.2">6</text></g>
    <circle cx="18" cy="123" r="7" fill="var(--blue)"/><circle cx="78" cy="123" r="7" fill="var(--blue)"/><g font-family="Montserrat,sans-serif" font-weight="800" fill="#fff" font-size="8" text-anchor="middle"><text x="18" y="126">A</text><text x="78" y="126">B</text></g></svg>
  <div style="left:44px;top:20px;width:32px"><div class="lbl" style="font-size:3.6px">LOREM IPSUM</div><div class="tiny">Phase six plan and key task.</div></div>
  <div style="left:129px;top:14px;width:36px"><div class="lbl" style="font-size:3.6px">LOREM IPSUM</div><div class="tiny">Phase five plan and key task.</div></div>
  <div style="left:190px;top:17px;width:36px"><div class="lbl" style="font-size:3.6px">LOREM IPSUM</div><div class="tiny">Phase three plan and key task.</div></div>
  <div style="left:91px;top:55px;width:32px"><div class="lbl" style="font-size:3.6px">LOREM IPSUM</div><div class="tiny">Phase two plan and key task.</div></div>
  <div style="left:180px;top:78px;width:32px"><div class="lbl" style="font-size:3.6px">LOREM IPSUM</div><div class="tiny">Phase one plan and key task.</div></div>
  <div class="h" style="left:10px;top:71px;font-size:8px;letter-spacing:.08em">TIMELINE OF</div>
  <div class="h b blue" style="left:10px;top:80px;font-size:12.5px">ROADMAP</div>
  <div class="h" style="left:11px;top:95px;font-size:5.8px;font-weight:700">FOR 2 YEARS</div>
  <div class="h b" style="left:28px;top:115px;font-size:7px">2019</div><div class="tiny" style="left:28px;top:123px;width:30px">Year one focus and aims.</div>
  <div class="h b" style="left:88px;top:115px;font-size:7px">2020</div><div class="tiny" style="left:88px;top:123px;width:30px">Year two focus and aims.</div>
  <div class="foot"><span>PLINTHWORKS</span><i>13</i></div>
</section>

<!-- 14 icons -->
<section class="slide" style="left:312px;top:693px">
  <svg class="deco" viewBox="0 0 271 153"><circle cx="150" cy="-4" r="22" fill="var(--blue)"/><circle cx="150" cy="-6" r="25" fill="none" stroke="var(--ink)" stroke-width="1.3"/><circle cx="262" cy="22" r="15" fill="none" stroke="var(--ink)" stroke-width="1.2"/><circle cx="55" cy="158" r="13" fill="var(--blue)"/><circle cx="55" cy="158" r="16" fill="none" stroke="var(--ink)" stroke-width="1.2"/>
    <g fill="none" stroke="var(--blue)" stroke-width=".7"><circle cx="183" cy="42" r="9"/><circle cx="183" cy="42" r="6.5" stroke-dasharray="1 1"/><circle cx="238" cy="42" r="9"/><circle cx="238" cy="42" r="6.5" stroke-dasharray="1 1"/><circle cx="183" cy="96" r="9"/><circle cx="183" cy="96" r="6.5" stroke-dasharray="1 1"/><circle cx="238" cy="96" r="9"/><circle cx="238" cy="96" r="6.5" stroke-dasharray="1 1"/></g>
    <g fill="none" stroke="var(--ink)" stroke-width=".6"><circle cx="183" cy="41" r="2.2"/><path d="M182 44v1.5h2V44"/><rect x="235" y="39" width="6" height="5"/><circle cx="183" cy="95" r="2.4"/><path d="M181.5 97l-1 3l2.5-1l2.5 1l-1-3"/><rect x="234" y="94" width="8" height="5"/><circle cx="238" cy="96.5" r="1.2"/></g></svg>
  <div class="h" style="left:11px;top:17px;font-size:10px">LOREM IPSUM</div>
  <div class="h b blue" style="left:11px;top:29px;font-size:10px">DOLOR SIT AMET</div>
  <div class="p" style="left:11px;top:45px;width:130px;text-align:justify"><p>Our services support each step of the plan. From the first brief to the final launch, the studio works with the client to set goals, shape designs and test them with real users before each release goes out.</p><p>Support stays in place after launch. The team reviews results, fixes issues and plans updates so the work keeps serving its goal.</p><p>Each service has a clear scope, an owner and a timeline, so the client always knows who is doing what and when it will be ready.</p></div>
  <div style="left:165px;top:55px;width:38px;text-align:center"><div class="lbl" style="font-size:3.8px">LOREM IPSUM</div><div class="tiny">Service line with a short note.</div></div>
  <div style="left:219px;top:55px;width:38px;text-align:center"><div class="lbl" style="font-size:3.8px">LOREM IPSUM</div><div class="tiny">Service line with a short note.</div></div>
  <div style="left:165px;top:109px;width:38px;text-align:center"><div class="lbl" style="font-size:3.8px">LOREM IPSUM</div><div class="tiny">Service line with a short note.</div></div>
  <div style="left:219px;top:109px;width:38px;text-align:center"><div class="lbl" style="font-size:3.8px">LOREM IPSUM</div><div class="tiny">Service line with a short note.</div></div>
  <div class="foot"><span>PLINTHWORKS</span><i>14</i></div>
</section>

<!-- 15 two columns -->
<section class="slide" style="left:596px;top:693px">
  <div style="left:25px;top:12px;width:117px;height:141px;background:var(--grey)"></div>
  <svg class="deco" viewBox="0 0 271 153"><circle cx="258" cy="19" r="5" fill="var(--blue)"/><circle cx="255" cy="-8" r="18" fill="none" stroke="var(--ink)" stroke-width="1.2"/><path d="M27 105 l3 2 l-3 2z" fill="var(--blue)"/><path d="M27 121 l3 2 l-3 2z" fill="none" stroke="var(--ink)" stroke-width=".5"/><path d="M150 105 l3 2 l-3 2z" fill="var(--ink)"/><path d="M150 121 l3 2 l-3 2z" fill="none" stroke="var(--blue)" stroke-width=".5"/></svg>
  <div class="h" style="left:26px;top:19px;font-size:8.6px">LOREM IPSUM</div>
  <div class="h b blue" style="left:26px;top:29px;font-size:8.6px">DOLOR SIT AMET</div>
  <div class="p" style="left:26px;top:41px;width:111px;text-align:justify"><p>Goals for the project are set out here, with the reason behind each one and the measure that will show when it has been met by the team.</p><p>Each goal links to the action steps that follow, so the client can see how the plan moves from idea to result on time.</p></div>
  <div class="tiny" style="left:34px;top:104px;width:104px">Short note on how this goal is measured.</div>
  <div class="tiny" style="left:34px;top:120px;width:104px">Short note on how this goal is measured.</div>
  <div class="h blue" style="left:150px;top:19px;font-size:8.6px">LOREM IPSUM</div>
  <div class="h b" style="left:150px;top:29px;font-size:8.6px">DOLOR SIT AMET</div>
  <div class="p" style="left:150px;top:41px;width:111px;text-align:justify"><p>Solutions show how each goal will be met, which tools the studio will use and how the work will be tested with the client.</p><p>Each solution links to a step on the timeline, so progress is easy to follow from start to finish.</p></div>
  <div class="tiny" style="left:157px;top:104px;width:104px">Short note on how this solution is delivered.</div>
  <div class="tiny" style="left:157px;top:120px;width:104px">Short note on how this solution is delivered.</div>
  <div class="foot"><span>PLINTHWORKS</span><i>15</i></div>
</section>

<!-- 16 timeline -->
<section class="slide" style="left:29px;top:858px">
  <svg class="deco" viewBox="0 0 271 153"><circle cx="4" cy="147" r="16" fill="var(--blue)"/><circle cx="4" cy="147" r="19" fill="none" stroke="var(--ink)" stroke-width="1.2"/><circle cx="254" cy="58" r="5" fill="var(--blue)"/><circle cx="280" cy="23" r="14" fill="none" stroke="var(--ink)" stroke-width="1.2"/><circle cx="246" cy="153" r="14" fill="none" stroke="var(--ink)" stroke-width="1.2"/>
    <path d="M36 88 H240" stroke="#999" stroke-width=".5"/>
    <g fill="none" stroke="var(--blue)" stroke-width="1.2"><path d="M46 88 V62 a17 17 0 0 1 34 0 V88"/><path d="M118 88 V62 a17 17 0 0 1 34 0 V88"/><path d="M189 88 V62 a17 17 0 0 1 34 0 V88"/></g>
    <g fill="none" stroke="var(--ink)" stroke-width="1.2"><path d="M82 88 V96 a17 17 0 0 0 34 0 V88"/><path d="M154 88 V96 a17 17 0 0 0 34 0 V88"/></g>
    <g fill="var(--blue)"><circle cx="63" cy="57" r="5"/><circle cx="135" cy="57" r="5"/><circle cx="206" cy="57" r="5"/></g><g fill="#fff"><circle cx="63" cy="57" r="2.8"/><circle cx="135" cy="57" r="2.8"/><circle cx="206" cy="57" r="2.8"/></g>
    <g fill="var(--ink)"><circle cx="99" cy="110" r="5"/><circle cx="171" cy="110" r="5"/></g><g fill="#fff"><circle cx="99" cy="110" r="2.8"/><circle cx="171" cy="110" r="2.8"/></g>
    <g font-family="Montserrat,sans-serif" font-size="8.4" text-anchor="middle" fill="var(--ink)"><text x="63" y="79">2018</text><text x="99" y="99">2019</text><text x="135" y="79">2020</text><text x="171" y="99">2021</text><text x="206" y="79">2022</text></g>
    <g fill="var(--ink)"><rect x="95" y="38" width="1.6" height="4"/><rect x="98" y="35" width="1.6" height="7"/><rect x="101" y="32" width="1.6" height="10"/><path d="M169 32 l6 2 l-3 2 l-1 4z"/><circle cx="63" cy="97" r="2"/><path d="M59 103 a4 3 0 0 1 8 0z"/><path d="M134 100 h2 v3 h-2z M135 94 a3 3 0 1 1 0 6 a3 3 0 1 1 0-6"/><text x="206" y="101" font-size="6" font-weight="700" text-anchor="middle" font-family="Montserrat,sans-serif">$</text></g></svg>
  <div class="h" style="left:48px;top:13px;font-size:9.5px;letter-spacing:.28em">TIMELINE</div>
  <div class="h b" style="left:115px;top:12px;font-size:9.5px;letter-spacing:.16em;background:var(--blue);color:#fff;padding:1px 3px">INFOGRAPHIC</div>
  <div style="left:82px;top:45px;width:34px;text-align:center"><div class="lbl blue" style="font-size:3.4px;color:var(--ink)">LOREM IPSUM</div><div class="tiny">Key step for this year with a short goal note.</div></div>
  <div style="left:154px;top:45px;width:34px;text-align:center"><div class="lbl" style="font-size:3.4px">LOREM IPSUM</div><div class="tiny">Key step for this year with a short goal note.</div></div>
  <div style="left:46px;top:105px;width:34px;text-align:center"><div class="lbl blue" style="font-size:3.4px">LOREM IPSUM</div><div class="tiny">Key step for this year with a short goal note.</div></div>
  <div style="left:118px;top:105px;width:34px;text-align:center"><div class="lbl blue" style="font-size:3.4px">LOREM IPSUM</div><div class="tiny">Key step for this year with a short goal note.</div></div>
  <div style="left:189px;top:105px;width:34px;text-align:center"><div class="lbl blue" style="font-size:3.4px">LOREM IPSUM</div><div class="tiny">Key step for this year with a short goal note.</div></div>
  <div class="foot"><span>PLINTHWORKS</span><i>16</i></div>
</section>

<!-- 17 benefits -->
<section class="slide" style="left:312px;top:858px">
  <div class="photo" style="left:15px;top:20px;width:133px;height:113px;background:linear-gradient(90deg,#fff 0%,#cfcfcf 30%,#8f8f8f 100%)" role="img" aria-label="Photo of a smiling team working at a computer"></div>
  <svg class="deco" viewBox="0 0 271 153"><circle cx="46" cy="126" r="12" fill="var(--blue)"/><circle cx="257" cy="7" r="12" fill="var(--blue)"/><circle cx="257" cy="7" r="15" fill="none" stroke="var(--ink)" stroke-width="1.2"/><circle cx="278" cy="140" r="14" fill="none" stroke="var(--ink)" stroke-width="1.2"/></svg>
  <div class="h" style="left:139px;top:23px;font-size:9.5px">BENEFITS TO EACH</div>
  <div class="h b blue" style="left:139px;top:34px;font-size:9.5px">CUSTOMER SEGMENTS</div>
  <div class="p" style="left:139px;top:47px;width:118px"><p>Labs gain a clear view of each project stage, with goals, owners and dates in one shared plan for all teams.</p><p>Research groups get designs that explain complex data simply, so results reach the right people fast and with less effort.</p><p>Start-ups gain a brand system that grows with them, ready for investors, partners and first clients.</p><p>Partners receive regular updates, so every team stays aligned on the same targets.</p><p>Clients keep full support after launch, with reviews and updates built into the timeline.</p></div>
  <div class="foot"><span>PLINTHWORKS</span><i>17</i></div>
</section>

<!-- 18 hub -->
<section class="slide" style="left:596px;top:858px">
  <svg class="deco" viewBox="0 0 271 153"><circle cx="252" cy="28" r="6" fill="var(--ink)"/><circle cx="282" cy="6" r="30" fill="none" stroke="var(--blue)" stroke-width="1.6"/>
    <g fill="none" stroke="var(--ink)" stroke-width="2.6"><circle cx="110" cy="80" r="14"/><circle cx="137" cy="56" r="14"/><circle cx="164" cy="56" r="14"/><circle cx="190" cy="80" r="14"/></g>
    <path d="M118 92 Q130 100 136 104 M182 92 Q170 100 164 104 M140 70 L145 94 M161 70 L156 94" stroke="var(--ink)" stroke-width="2.4" fill="none"/>
    <circle cx="150" cy="107" r="15" fill="var(--blue)" stroke="var(--ink)" stroke-width="2.6"/><circle cx="150" cy="107" r="11" fill="none" stroke="#fff" stroke-width=".6" stroke-dasharray="1.5 1"/>
    <g fill="var(--blue)"><circle cx="124" cy="82" r="3"/><circle cx="150" cy="60" r="3"/><circle cx="176" cy="66" r="3"/><circle cx="202" cy="86" r="3"/></g>
    <g fill="var(--ink)"><path d="M105 76 l5-2 l5 2 l-5 2z M107 77 v3 h6 v-3"/><rect x="133" y="49" width="8" height="5"/><path d="M158 52 l6-2 l6 2 l-6 2z"/><rect x="186" y="75" width="8" height="6"/></g>
    <g font-family="Montserrat,sans-serif" font-size="3.6" font-weight="700" fill="var(--ink)" text-anchor="middle"><text x="110" y="88">Option A</text><text x="137" y="62">Option B</text><text x="164" y="62">Option C</text><text x="190" y="88">Option D</text><text x="150" y="109" fill="#fff" font-size="3.4">PLINTHWORKS</text></g></svg>
  <div class="h" style="left:16px;top:9px;font-size:9.5px">LOREM IPSUM <span class="b blue">DOLOR SIT AMET</span></div>
  <div style="left:96px;top:30px;width:30px;text-align:right"><div class="lbl blue" style="font-size:3.8px">Your Title</div><div class="tiny">Short note on this option.</div></div>
  <div style="left:174px;top:28px;width:30px"><div class="lbl blue" style="font-size:3.8px">Your Title</div><div class="tiny">Short note on this option.</div></div>
  <div style="left:58px;top:69px;width:32px;text-align:right"><div class="lbl blue" style="font-size:3.8px">Your Title</div><div class="tiny">Short note on this option.</div></div>
  <div style="left:210px;top:69px;width:32px"><div class="lbl blue" style="font-size:3.8px">Your Title</div><div class="tiny">Short note on this option.</div></div>
  <div class="p" style="left:30px;top:127px;width:211px;text-align:center">Each option links back to a goal in the plan. The studio will compare cost, time and impact before the team agrees on the path forward.</div>
  <div class="foot"><span>PLINTHWORKS</span><i>18</i></div>
</section>

<!-- 19 terms -->
<section class="slide" style="left:29px;top:1023px">
  <svg class="deco" viewBox="0 0 271 153"><circle cx="227" cy="21" r="8" fill="var(--blue)"/><circle cx="246" cy="28" r="18" fill="none" stroke="var(--ink)" stroke-width="1.3"/><circle cx="0" cy="20" r="10" fill="none" stroke="var(--ink)" stroke-width="1.2"/><circle cx="62" cy="157" r="18" fill="var(--blue)"/><circle cx="62" cy="157" r="21" fill="none" stroke="var(--ink)" stroke-width="1.2"/>
    <g fill="#fff" stroke="var(--ink)" stroke-width="1.2"><rect x="21" y="20" width="28" height="65" rx="3"/><rect x="62" y="40" width="28" height="65" rx="3"/><rect x="103" y="60" width="28" height="65" rx="3"/></g>
    <g fill="var(--ink)"><rect x="30" y="22" width="10" height="1.4" rx=".7"/><rect x="71" y="42" width="10" height="1.4" rx=".7"/><rect x="112" y="62" width="10" height="1.4" rx=".7"/></g>
    <g fill="none" stroke="var(--blue)" stroke-width=".6"><rect x="31" y="56" width="6" height="5"/><rect x="72" y="76" width="6" height="5"/><rect x="113" y="96" width="6" height="5"/></g></svg>
  <div style="left:24px;top:28px;font-size:4.2px;font-style:italic;font-weight:600;width:24px">Lorem ipsum dolor</div>
  <div class="tiny" style="left:24px;top:64px;width:22px;font-size:2.2px">Intro to the terms and the scope of the work.</div>
  <div style="left:65px;top:48px;font-size:4.2px;font-style:italic;font-weight:600;width:24px">Dolor sit amet, conse</div>
  <div class="tiny" style="left:65px;top:84px;width:22px;font-size:2.2px">Payment terms and the schedule for each stage.</div>
  <div style="left:106px;top:68px;font-size:4.2px;font-style:italic;font-weight:600">Consec</div>
  <div class="tiny" style="left:106px;top:104px;width:22px;font-size:2.2px">Rights, reviews and sign-off for final files.</div>
  <div class="h" style="left:143px;top:49px;font-size:8.6px">OUR COMPANY</div>
  <div class="h b blue" style="left:143px;top:60px;font-size:8.6px">TERMS &amp; CONDITIONS</div>
  <div class="p" style="left:143px;top:73px;width:118px"><p>These terms set out how the studio and the client work together, from the first brief to final delivery and support after launch.</p><p>Fees, timelines and reviews are agreed before work starts, and any change to scope is confirmed in writing by both sides.</p><p>All final files pass to the client on full payment, with source files kept safe for later use.</p></div>
  <div class="foot"><span>PLINTHWORKS</span><i>19</i></div>
</section>

<!-- 20 team -->
<section class="slide" style="left:312px;top:1023px">
  <div style="left:0;top:64px;width:271px;height:63px;background:var(--blue)"></div>
  <svg class="deco" viewBox="0 0 271 153"><g fill="#fff" stroke="var(--ink)" stroke-width="1.2"><circle cx="38" cy="79" r="11"/><circle cx="103" cy="79" r="11"/><circle cx="168" cy="79" r="11"/><circle cx="232" cy="79" r="11"/></g></svg>
  <div style="left:30px;top:71px;width:16px;height:16px;border-radius:50%;background:linear-gradient(#cfcfcf,#8d8d8d)" role="img" aria-label="Team member portrait"></div>
  <div style="left:95px;top:71px;width:16px;height:16px;border-radius:50%;background:linear-gradient(#cfcfcf,#8d8d8d)" role="img" aria-label="Team member portrait"></div>
  <div style="left:160px;top:71px;width:16px;height:16px;border-radius:50%;background:linear-gradient(#cfcfcf,#8d8d8d)" role="img" aria-label="Team member portrait"></div>
  <div style="left:224px;top:71px;width:16px;height:16px;border-radius:50%;background:linear-gradient(#cfcfcf,#8d8d8d)" role="img" aria-label="Team member portrait"></div>
  <div class="h" style="left:0;top:16px;width:271px;text-align:center;font-size:8.6px">TEAM MEMBERS <span class="b blue">AND ADVISORS</span></div>
  <div class="p" style="left:18px;top:29px;width:235px;text-align:center"><p>Our team brings design, research and tech skills together. Each member owns a part of the plan and works closely with the client from brief to launch and beyond.</p><p>Advisors from the biotech field review key steps and help keep the work accurate.</p></div>
  <div style="left:18px;top:93px;width:40px;text-align:center"><div class="lbl" style="font-size:4px;color:var(--ink)">OWEN HALE</div><div class="tiny" style="color:#fff">Lead designer, owns brand and layout.</div></div>
  <div style="left:83px;top:93px;width:40px;text-align:center"><div class="lbl" style="font-size:4px;color:var(--ink)">LENA MARSH</div><div class="tiny" style="color:#fff">Project lead, owns plan and timeline.</div></div>
  <div style="left:148px;top:93px;width:40px;text-align:center"><div class="lbl" style="font-size:4px;color:var(--ink)">OWEN HALE</div><div class="tiny" style="color:#fff">Tech lead, owns build and testing.</div></div>
  <div style="left:212px;top:93px;width:40px;text-align:center"><div class="lbl" style="font-size:4px;color:var(--ink)">LENA MARSH</div><div class="tiny" style="color:#fff">Research lead, owns data and review.</div></div>
  <div class="foot"><span>PLINTHWORKS</span><i>20</i></div>
</section>

<!-- 21 thank you -->
<section class="slide" style="left:596px;top:1023px">
  <div class="photo" style="left:110px;top:0;width:161px;height:153px;background:linear-gradient(90deg,#fff 0%,#e6e6e6 25%,#9a9a9a 100%)" role="img" aria-label="Photo of a businesswoman holding a phone"></div>
  <div class="brand" style="left:16px;top:15px;font-size:13px">PLINTHWORKS</div>
  <div class="h b" style="left:16px;top:55px;font-size:14px">THANK YOU</div>
  <div class="h b" style="left:16px;top:83px;font-size:8.6px">CONTACT <span class="blue">US</span></div>
  <div style="left:16px;top:96px;font-size:5.4px;line-height:1.6;color:#444">
    <div><span class="blue">●</span> 555-018-274</div>
    <div><span class="blue">●</span> info@plinthworks.co</div>
    <div><span class="blue">●</span> Your address, your city, box 88900</div>
  </div>
  <div style="left:16px;top:132px;width:6px;height:6px;background:var(--blue)"></div>
  <div style="left:26px;top:132px;font-size:4.8px;letter-spacing:.2em;font-weight:600">www.plinthworks.co</div>
</section>

</body>
</html>
```